LUMEN Environmental needs an upgrade to its current business cards design

We need an upgrade to our current business cards design, where the LUMEN acronym is included, as possible and not being overloaded.
LUMEN Environmental is an Environmental Consultancy Firm based in Sydney.
We would like to see creative designs different from the standard type of business cards (for example, rounded edges, different to standard size of common business cards.

Target Market(s)

industrial companies (oil & gas, petrochemical, mining, insolvency, finance and manufacturing), developers, architect firms, law firms.

Industry/Entity Type

Business

Contact Information for Business Card

logos (brand and acronym), if they don't appear overloaded.
name
role
name of company (LUMEN Environmental),
address (Level 4, Suite 4B, 72-76 Wrenfield Street, Marlow Vale, NSW, 2093) landline (02 7314 2286)
mobile (staff member)
email (staff member) and
website (www.lumenverda.example).
Include: Contaminated Land, Site Remediation, Groundwater Assessment, Health and Ecological Risk Assessments, Acid Sulfate Soils, Waste Classification.

Font styles to use
Serif
Sans Serif

Requirements
Must have
• A creative design different to the standard type of business cards.
Nice to have
• Rounded edges
• Different size of business cards rather than the standard size.
Should not have
• Preferable not to use white colour background, unless it is required from a creative design proposed.
• Not an overloaded design.
• Avoid black colours

```html
<!DOCTYPE html>
<html lang="en">
<head>
<meta charset="utf-8">
<title>LUMEN Environmental – Business Cards</title>
<link href="https://fonts.googleapis.com/css2?family=Montserrat:wght@400;500;700&display=swap" rel="stylesheet">
<style>
  :root {
    --backdrop: #2e2e2e;
    --card: #050505;
    --green: #6cc13f;
    --grey: #8a8a8a;
    --text: #e9e9e9;
    --divider: #6a6a6a;
  }
  * { margin: 0; padding: 0; box-sizing: border-box; }
  html, body {
    width: 1200px; height: 900px; overflow: hidden;
    background: var(--backdrop);
    font-family: "Montserrat", sans-serif;
  }
  .canvas { position: relative; width: 1200px; height: 900px; }
  .card {
    position: absolute;
    width: 620px; height: 360px;
    background: var(--card);
    border-radius: 28px;
    overflow: hidden;
    box-shadow: 0 18px 40px rgba(0,0,0,0.55);
  }
  .card--front { left: 90px; top: 60px; }
  .card--back { left: 490px; top: 480px; }

  .brand-name {
    font-weight: 700;
    color: var(--grey);
    letter-spacing: 1px;
    white-space: nowrap;
  }

  /* Front */
  .card--front .brand-name {
    position: absolute; top: 78px; left: 0; width: 100%;
    text-align: center; font-size: 40px;
  }
  .services {
    position: absolute; top: 160px; left: 0; width: 100%;
    list-style: none; text-align: center;
    color: var(--text); font-size: 17px; line-height: 24px;
  }

  /* Back */
  .accent-band {
    position: absolute; right: 0; top: 0;
    width: 16px; height: 175px;
    background: var(--green);
    border-bottom-left-radius: 10px;
  }
  .card--back .brand-name {
    position: absolute; left: 34px; top: 200px;
    font-size: 20px;
  }
  .divider {
    position: absolute; left: 330px; top: 48px;
    width: 1px; height: 265px;
    background: var(--divider);
  }
  .contact {
    position: absolute; left: 352px; top: 70px; right: 30px;
    color: var(--text); font-size: 14px; line-height: 20px;
  }
  .contact__name {
    color: var(--green); font-size: 22px; font-weight: 500;
    letter-spacing: 0.5px; line-height: 28px; white-space: nowrap;
  }
  .contact__role { margin-bottom: 12px; }
  .contact__address { margin-bottom: 10px; white-space: nowrap; }
  .contact__line { display: flex; align-items: center; gap: 8px; white-space: nowrap; }
  .contact__line svg { width: 12px; height: 12px; flex: none; }
  .highlight { color: var(--green); }
</style>
</head>
<body>
<div class="canvas">

  <section class="card card--front">
    <div class="brand-name">LUMEN Environmental</div>
    <ul class="services">
      <li>Contaminated Land</li>
      <li>Site Remediation</li>
      <li>Groundwater Assessment</li>
      <li>Health and Ecological Risk Assessments</li>
      <li>Acid Sulfate Soils</li>
      <li>Waste Classification</li>
    </ul>
  </section>

  <section class="card card--back">
    <div class="accent-band"></div>
    <div class="brand-name">LUMEN Environmental</div>
    <div class="divider"></div>
    <div class="contact">
      <div class="contact__name">ROWAN KESSLER</div>
      <div class="contact__role">Project Engineer</div>
      <div class="contact__address">
        Level 4, Suite 4B,<br>
        72-76 Wrenfield Street,<br>
        Marlow Vale, NSW, 2093
      </div>
      <div class="contact__line">
        <svg viewBox="0 0 12 12"><path d="M2.5 1l2 2.2-1 1.3c.7 1.5 1.8 2.6 3.2 3.2l1.3-1 2.2 2-1.2 1.6C5.3 10 2 6.7 1.3 2.2z" fill="var(--green)"/></svg>
        (02 7314 2286)
      </div>
      <div class="contact__line">
        <svg viewBox="0 0 12 12"><rect x="1" y="2.5" width="10" height="7" rx="1" fill="none" stroke="var(--green)" stroke-width="1.2"/><path d="M1.5 3l4.5 3.5L10.5 3" fill="none" stroke="var(--green)" stroke-width="1.2"/></svg>
        rowan@lumenverda.example
      </div>
      <div class="contact__line">
        <svg viewBox="0 0 12 12"><circle cx="6" cy="6" r="4.8" fill="none" stroke="var(--green)" stroke-width="1.2"/><path d="M1.2 6h9.6M6 1.2c-2 2.6-2 7 0 9.6M6 1.2c2 2.6 2 7 0 9.6" fill="none" stroke="var(--green)" stroke-width="1"/></svg>
        <span>www.<span class="highlight">lumenverda.example</span></span>
      </div>
    </div>
  </section>

</div>
</body>
</html>
```